Company or website name
- Marla Quist Design & Decor
- Passionate about wedding floral design and decor. Events I create are timeless, classic and elegant, customized 100% to the brides’ desires. Inspiring them with a vision of what is possible & asking them to step inside it and see it for themselves

```html
<!DOCTYPE html>
<html lang="en">
<head>
<meta charset="utf-8">
<title>Marla Quist Design &amp; Decor — Stationery</title>
<link rel="stylesheet" href="https://fonts.googleapis.com/css2?family=Open+Sans:wght@400;600&family=Tinos:wght@400&display=swap">
<style>
  :root {
    --paper: #ffffff;
    --bg: #ffffff;
    --rose: #ef6a8f;
    --rose-deep: #e2346f;
    --rose-text: #e4608a;
    --grey-text: #a3a3a3;
    --edge: #e2e2e2;
    --white: #ffffff;
  }
  * { box-sizing: border-box; margin: 0; padding: 0; }
  html, body { width: 1200px; height: 961px; overflow: hidden; background: var(--bg); }
  .canvas { position: relative; width: 1200px; height: 961px; }

  .brand-mark { position: absolute; border-radius: 50%; background: var(--rose-deep); }
  .brand-name {
    position: absolute; color: var(--rose-text); font-weight: 400;
    font-family: "Open Sans", sans-serif; line-height: 1.1; white-space: nowrap;
  }
  .brand-name .line-main { display: block; }
  .brand-name .line-sub { display: block; letter-spacing: 0.3em; }

  .letterhead {
    position: absolute; left: 172px; top: 125px; width: 471px; height: 667px;
    background: var(--paper); border: 1px solid var(--edge);
    font-family: "Open Sans", sans-serif;
  }
  .letterhead .brand-mark { left: 22px; top: 42px; width: 34px; height: 34px; }
  .letterhead .brand-name { left: 110px; top: 38px; }
  .letterhead .line-main { font-size: 26px; }
  .letterhead .line-sub { font-size: 10px; margin-top: 4px; }
  .letterhead-footer {
    position: absolute; left: 0; right: 0; bottom: 22px;
    text-align: center; color: var(--grey-text); font-size: 9.5px; line-height: 12px;
  }
  .letterhead-footer span { margin: 0 4px; }
  .letterhead-band { position: absolute; left: 0; right: 0; bottom: 0; height: 16px; background: var(--rose); }

  .card-front {
    position: absolute; left: 771px; top: 283px; width: 260px; height: 156px;
    background: var(--paper); border: 1px solid var(--edge); overflow: hidden;
  }
  .card-front .brand-mark { left: 22px; top: 72px; width: 28px; height: 28px; }
  .card-front .brand-name { left: 118px; top: 62px; }
  .card-front .line-main { font-size: 19px; }
  .card-front .line-sub { font-size: 7.5px; margin-top: 3px; }

  .card-back {
    position: absolute; left: 793px; top: 555px; width: 261px; height: 158px;
    background: var(--rose); border: 1px solid var(--edge);
    overflow: hidden; font-family: "Tinos", serif;
  }
  .card-back .strip-h { position: absolute; left: 0; right: 0; top: 21px; height: 51px; background: var(--white); }
  .card-back .strip-v { position: absolute; top: 0; bottom: 0; left: 131px; width: 8px; background: var(--white); }
  .card-back .brand-name { left: 14px; top: 94px; color: var(--white); }
  .card-back .line-main { font-size: 19px; }
  .card-back .line-sub { font-size: 7.5px; margin-top: 3px; }
  .card-contact {
    position: absolute; right: 10px; top: 76px; text-align: right;
    color: var(--white); font-size: 7px; line-height: 11px; white-space: nowrap;
  }
  .card-contact .address { margin-top: 10px; line-height: 13px; }
</style>
</head>
<body>
<main class="canvas">

  <section class="letterhead">
    <span class="brand-mark"></span>
    <div class="brand-name">
      <span class="line-main">Marla Quist</span>
      <span class="line-sub">Design &amp; Decor</span>
    </div>
    <div class="letterhead-footer">
      <div><span>Phone : 123-456-789</span><span>Fax : 123-456-789</span><span>Email : youremail</span></div>
      <div><span>Website : www.MarlaQuist.com</span><span>Address : PO Box 12345, city, AB 12345</span></div>
    </div>
    <div class="letterhead-band"></div>
  </section>

  <section class="card-front">
    <span class="brand-mark"></span>
    <div class="brand-name">
      <span class="line-main">Marla Quist</span>
      <span class="line-sub">Design &amp; Decor</span>
    </div>
  </section>

  <section class="card-back">
    <div class="strip-h"></div>
    <div class="strip-v"></div>
    <div class="brand-name">
      <span class="line-main">Marla Quist</span>
      <span class="line-sub">Design &amp; Decor</span>
    </div>
    <div class="card-contact">
      <div>P : 123-456-7890</div>
      <div>C : 123-456-7890</div>
      <div>F : 123-456-7890</div>
      <div>E : studio@marlaquist.com</div>
      <div class="address">123 New Street #456<br>San Francisco CA, 12345</div>
    </div>
  </section>

</main>
</body>
</html>
```